Premium modern eliquids labels 84.5 x 80 mm

I am looking for modern graphics for the labels of a new eliquid line that will have 4 different types of eliquids. It will have a tobacco one (brown colours maybe), a fruity one (bright colours maybe), a minty one (green colours maybe) and a creamy one (beige colours maybe).
I will need one of them to see how the design is, that design will have to be adapted to the other 3 colours of the label.
The brand logo is attached. I also attached a sample of what is mandatory to write on the label, you can change size, place and font of what is written, the only thing that cannot be reduced is the yellow parts. I attach the bottle that we will use.The size of the label is 84.5 x 80 mm (base x height).

Target Market(s)

vapers

Requirements
Must have
• My project must have one of the labels.

```html
<!DOCTYPE html>
<html lang="it">
<head>
<meta charset="utf-8">
<title>Tobacco – etichetta e-liquid</title>
<link rel="stylesheet" href="https://fonts.googleapis.com/css2?family=Roboto+Condensed:wght@700&family=Arimo:wght@400;700&family=Abril+Fatface&display=swap">
<style>
  :root {
    --page-bg: #1d1d1d;
    --band-brown: #3d2215;
    --flavour-ink: #b9a393;
    --label-ink: #ffffff;
    --badge-yellow: #f7c21a;
    --badge-ink: #111111;
  }
  * { margin: 0; padding: 0; box-sizing: border-box; }
  html, body { width: 1200px; height: 1200px; overflow: hidden; background: var(--page-bg); }
  .label {
    position: absolute; left: 70px; top: 98px; width: 1060px; height: 1003px;
    overflow: hidden; color: var(--label-ink);
  }
  .label-art {
    position: absolute; inset: 0;
    background:
      radial-gradient(ellipse 30% 22% at 40% 62%, rgba(214,230,120,.75), transparent 70%),
      radial-gradient(ellipse 28% 24% at 62% 68%, rgba(246,150,90,.7), transparent 70%),
      radial-gradient(ellipse 40% 25% at 50% 88%, rgba(236,80,160,.6), transparent 70%),
      linear-gradient(180deg, #1f1f1f 0%, #3a2a38 20%, #7a5a6a 38%, #c45a9a 62%, #e0579f 100%);
  }
  .text-block { position: absolute; font-family: "Roboto Condensed", "Arial Narrow", sans-serif; font-weight: 700; font-size: 29px; line-height: 31px; }
  .ingredients { left: 32px; top: 24px; width: 240px; }
  .instructions { left: 842px; top: 24px; width: 200px; }
  .flavour-band {
    position: absolute; left: 0; top: 395px; width: 100%; height: 100px;
    background: var(--band-brown); display: flex; align-items: center; justify-content: center;
  }
  .flavour-name { font-family: "Abril Fatface", serif; font-size: 46px; color: var(--flavour-ink); letter-spacing: 1px; }
  .batch-code {
    position: absolute; left: 62px; top: 730px; transform: rotate(-90deg); transform-origin: 0 0;
    font-family: "Roboto Condensed", sans-serif; font-weight: 700; font-size: 20px; white-space: nowrap;
  }
  .producer { position: absolute; left: 32px; top: 756px; font-family: Arimo, Arial, sans-serif; font-weight: 700; font-size: 22px; line-height: 24px; }
  .producer .lead { font-size: 23px; letter-spacing: .5px; }
  .net-small { position: absolute; left: 505px; top: 910px; font-family: "Roboto Condensed", sans-serif; font-weight: 700; font-size: 17px; }
  .net-large { position: absolute; left: 860px; top: 918px; font-family: "Roboto Condensed", sans-serif; font-weight: 700; font-size: 26px; }
  .badge {
    position: absolute; background: var(--badge-yellow); color: var(--badge-ink);
    font-family: Arimo, Arial, sans-serif; font-weight: 700; text-align: center;
  }
  .badge-collect { left: 863px; width: 150px; height: 48px; font-size: 20px; line-height: 19px; padding-top: 5px; }
  .badge-code { left: 863px; width: 108px; height: 45px; font-size: 24px; line-height: 45px; letter-spacing: 1px; }
  .badge-caption { position: absolute; left: 866px; font-family: Arimo, Arial, sans-serif; font-weight: 700; font-size: 17px; }
  .disposal-icons { position: absolute; left: 852px; top: 820px; }
</style>
</head>
<body>
<main class="label">
  <div class="label-art" role="img" aria-label="Astratto fluido con bolle colorate in giallo, arancio, verde e magenta su fondo scuro"></div>

  <p class="text-block ingredients">INGREDIENTI:<br>GLICOLE<br>PROPILENICO<br>SOSTANZE<br>AROMATIZZANTI</p>
  <p class="text-block instructions">ISTRUZIONI<br>D’USO:<br>Agitare bene prima dell’utilizzo. Diluire nelle percentuali consigliate sul nostro sito. Conservare in luogo fresco e asciutto</p>

  <div class="flavour-band"><h1 class="flavour-name">tobacco</h1></div>

  <p class="batch-code">L.SH20 - 001-PES-D PROD 22-04-2022 D.SC.21-04-2024</p>

  <address class="producer" style="font-style:normal">
    <span class="lead">PRODOTTO<br>E CONFEZIONATO<br>DA Lumen Aromi srl</span><br>
    Via Solferino 18<br>10121 Torino<br>P.i.01234567890<br>Tel. +39 011 5550192<br>info@lumenaromi.it
  </address>

  <p class="net-small">20 ML NET</p>

  <div class="badge badge-collect" style="top:483px">RACCOLTA<br>PLASTICA</div>
  <p class="badge-caption" style="top:540px">ETICHETTA</p>
  <div class="badge badge-code" style="top:562px">PAP 5</div>

  <div class="badge badge-collect" style="top:633px">RACCOLTA<br>PLASTICA</div>
  <p class="badge-caption" style="top:692px;left:872px">FLACONE</p>
  <div class="badge badge-code" style="top:710px">PET 1</div>

  <svg class="disposal-icons" width="170" height="75" viewBox="0 0 170 75" fill="none" stroke="#fff" stroke-width="3" aria-label="Riciclo e smaltimento">
    <g>
      <path d="M28 10 L40 30 M40 30 l-10 -2 M40 30 l2 -10"/>
      <path d="M56 50 L32 50 M32 50 l8 -7 M32 50 l8 7"/>
      <path d="M12 50 L24 28 M24 28 l-1 10 M24 28 l-9 4"/>
      <path d="M22 12 L6 40 L14 56 M60 46 L46 18 L34 16 M20 60 L52 60 L62 50"/>
    </g>
    <g fill="#fff" stroke="none">
      <circle cx="140" cy="8" r="7"/>
      <rect x="132" y="18" width="16" height="32" rx="4"/>
      <rect x="133" y="48" width="6" height="24"/>
      <rect x="141" y="48" width="6" height="24"/>
    </g>
    <path d="M90 36 L96 72 L118 72 L124 36 Z M88 36 H126 M124 38 L134 24" stroke="#fff"/>
    <path d="M102 20 l3 8 M110 18 l0 9" stroke="#fff"/>
  </svg>

  <p class="net-large">20 ML NET</p>
</main>
</body>
</html>
```